Corvix Energy Battery advertisment for Facebook ads

Objective:
Design a compelling Facebook advertisement to promote the new Federal Government Home Battery Subsidy, encouraging existing solar customers to act now and install a battery system under the new subsidy program.

Key Message:

25kWh Battery System Installed from $9,800
Act now and secure your affordable energy future today!
Design Requirements:

Bold headline showcasing the 25kWh for $9,800 offer.
Clear reference to the Federal Government Battery Subsidy as the reason for the low pricing.
Include messaging around:
Claim your subsidy before it winds down—like the solar rebate, it reduces each year
The subsidy can only be claimed once per household—go large now to future-proof your energy needs
Add a strong Call to Action like: “Beat the Rush—Secure Your Battery Today!”

Target Market(s)

Home owners who want to add batteries to existing solar systems

Industry/Entity Type

Renewable energy

Colors
0054AA
0677BA
7BADD7
CADEEF
E8F1F8
EB3D1F
EC4F4E
F09395
F8D3D4
FCEDEE

Requirements
Must have
• Visual Style: Modern, clean, and high-trust Use imagery of solar homes, battery units, or families enjoying power security at night Include visual cues of savings, energy independence, or clean energy Mobile-optimized, designed for Facebook feed
Nice to have
• Tone: Confident, future-focused, and urgent—while remaining trustworthy and informative. I would like a picture of battery ideally TQM battery on a home or such
Should not have
• must be professional and be a call to action

```html
<!DOCTYPE html>
<html lang="en">
<head>
<meta charset="UTF-8">
<title>Corvix Energy – 25kWh Battery Facebook Ad</title>
<link rel="stylesheet" href="https://fonts.googleapis.com/css2?family=Poppins:ital,wght@0,400;0,500;0,600;0,700;0,800;1,500;1,700;1,800&display=swap">
<style>
  :root {
    --brand-red: #c01f2f;
    --brand-navy: #2d3446;
    --paper: #ffffff;
    --sky: #9cc3ea;
    --sky-deep: #6f98cf;
    --panel-blue: #33457a;
    --panel-dark: #27335c;
    --unit-white: #e9ecef;
    --hat-orange: #f07a2a;
  }
  * { margin: 0; padding: 0; box-sizing: border-box; }
  html, body {
    width: 1200px; height: 1200px; overflow: hidden;
    background: var(--paper);
    font-family: "Poppins", sans-serif;
  }
  .ad {
    position: relative;
    width: 1200px; height: 1200px;
    overflow: hidden;
    background: var(--paper);
  }
  .ad-shapes {
    position: absolute; inset: 0;
    width: 1200px; height: 1200px;
  }
  .headline { position: absolute; left: 64px; top: 40px; color: var(--brand-navy); }
  .headline-capacity {
    display: block;
    font-size: 142px; font-weight: 700; line-height: 1;
    letter-spacing: -3px;
    color: var(--brand-red);
  }
  .headline-product {
    display: block;
    margin-top: 8px;
    font-size: 53px; font-weight: 500; line-height: 61px;
    letter-spacing: 0.5px;
  }
  .headline-price {
    position: absolute; left: 36px; top: 310px;
    display: flex; align-items: flex-start;
    color: var(--brand-navy);
    font-weight: 700;
  }
  .headline-price .currency { font-size: 40px; line-height: 1; margin-top: 12px; margin-right: 4px; }
  .headline-price .amount { font-size: 94px; line-height: 1; letter-spacing: -1px; }
  .price-underline {
    position: absolute; left: 67px; top: 428px;
    width: 105px; height: 15px;
    background: var(--brand-red);
  }
  .subsidy {
    position: absolute; right: 37px; top: 62px;
    width: 420px;
    text-align: right;
    color: var(--paper);
    font-style: italic;
  }
  .subsidy-title {
    font-size: 31px; font-weight: 800; line-height: 36px;
    letter-spacing: 0.2px;
  }
  .subsidy-point {
    margin-top: 18px;
    font-size: 17.5px; font-weight: 500; line-height: 22px;
  }
  .subsidy-point + .subsidy-point { margin-top: 10px; }
  .cta {
    position: absolute; left: 67px; top: 1020px;
    color: var(--paper);
    font-size: 43px; font-weight: 700; line-height: 56px;
    letter-spacing: -0.3px;
  }
  .cta-lead { display: block; font-style: italic; }
  .brand {
    position: absolute; left: 830px; top: 1040px;
    width: 350px;
  }
  .brand-row { display: flex; align-items: center; gap: 14px; }
  .brand-mark { width: 60px; height: 60px; background: var(--brand-red); flex: none; }
  .brand-name {
    color: var(--brand-navy);
    font-size: 37px; font-weight: 600; line-height: 1.1;
    letter-spacing: -0.5px;
  }
  .brand-tagline {
    margin-top: 16px;
    color: var(--brand-navy);
    font-size: 15.5px; font-weight: 400;
    letter-spacing: -0.2px;
    white-space: nowrap;
  }
</style>
</head>
<body>
<main class="ad">
  <svg class="ad-shapes" viewBox="0 0 1080 1080" preserveAspectRatio="none">
    <defs>
      <linearGradient id="photo-base" x1="1" y1="0" x2="0" y2="1">
        <stop offset="0" stop-color="var(--sky)"/>
        <stop offset="0.35" stop-color="var(--sky-deep)"/>
        <stop offset="0.7" stop-color="var(--panel-blue)"/>
        <stop offset="1" stop-color="var(--panel-dark)"/>
      </linearGradient>
      <radialGradient id="photo-light" cx="0.36" cy="0.68" r="0.32">
        <stop offset="0" stop-color="var(--unit-white)" stop-opacity="0.85"/>
        <stop offset="0.6" stop-color="var(--unit-white)" stop-opacity="0.35"/>
        <stop offset="1" stop-color="var(--unit-white)" stop-opacity="0"/>
      </radialGradient>
      <radialGradient id="photo-warm" cx="0.7" cy="0.38" r="0.24">
        <stop offset="0" stop-color="var(--hat-orange)" stop-opacity="0.55"/>
        <stop offset="1" stop-color="var(--hat-orange)" stop-opacity="0"/>
      </radialGradient>
      <clipPath id="photo-clip">
        <path d="M0,475 L340,475 C480,460 580,360 620,210 C640,130 650,60 660,0 L1080,0 L1080,870 L0,870 Z"/>
      </clipPath>
    </defs>
    <g role="img" aria-label="Photo: technician in an orange hard hat fixing a white home battery stack and inverter beside rooftop solar panels under a blue sky" clip-path="url(#photo-clip)">
      <rect fill="url(#photo-base)" x="0" y="0" width="1080" height="870"/>
      <rect fill="url(#photo-warm)" x="0" y="0" width="1080" height="870"/>
      <rect fill="url(#photo-light)" x="0" y="0" width="1080" height="870"/>
    </g>
    <path class="swoosh" fill="var(--brand-red)" d="M0,445 L340,445 C470,425 560,320 598,185 C618,115 630,55 642,0 L662,0 C652,60 642,130 622,212 C582,362 482,462 340,475 L0,475 Z"/>
    <path class="subsidy-panel" fill="var(--brand-navy)" d="M662,0 L1080,0 L1080,302 L710,302 C660,302 622,272 610,236 C630,160 648,80 662,0 Z"/>
    <rect class="cta-band" fill="var(--brand-red)" x="0" y="870" width="800" height="172"/>
    <path class="brand-corner" fill="var(--paper)" d="M680,1080 L680,1042 C692,932 752,846 880,840 L1080,840 L1080,1080 Z"/>
    <rect fill="var(--paper)" x="0" y="1042" width="1080" height="38"/>
  </svg>

  <h1 class="headline">
    <span class="headline-capacity">25kWh</span>
    <span class="headline-product">Battery System<br>Installed from</span>
  </h1>
  <p class="headline-price"><span class="currency">$</span><span class="amount">9,800</span></p>
  <div class="price-underline"></div>

  <section class="subsidy">
    <h2 class="subsidy-title">Federal Government<br>Subsidy is coming</h2>
    <p class="subsidy-point">Claim your subsidy before it winds down—like<br>the solar rebate, it reduces each year.</p>
    <p class="subsidy-point">The subsidy can only be claimed once per household—go large now to future-proof your energy needs.</p>
  </section>

  <p class="cta"><span class="cta-lead">Beat the Rush</span>Secure Your Battery Today!</p>

  <div class="brand">
    <div class="brand-row">
      <span class="brand-mark"></span>
      <span class="brand-name">Corvix Energy</span>
    </div>
    <p class="brand-tagline">ENGINEERING AND ECONOMIC SOLUTIONS</p>
  </div>
</main>
</body>
</html>
```